SAVOR food + music festival poster

11x17 poster design for our food & music festival in Lexington, KY. The two-day festival is a celebration of all things local and over 20,000 people attend each year. Over 50 local food vendors and food trucks, local music, craft beer and cocktails, a car show, kids activities, art etc. www.savorfestplex.com. Attached is our logo, and variation thereof. We prefer the black text with yellow "nom" as well call him. Images: https://shortlinkr.com/q4kd9wza and https://shortlinkr.com/p7ht2mue and https://shortlinkr.com/r3vn8bqc and https://shortlinkr.com/w5jx1fsd

Target Market(s)

People who would want to attend a food and music festival

Industry/Entity Type

Festival

Font styles to use
Sans Serif

Colors

Designer to choose colors to be used in the design.

Requirements
Must have
• (savor logo)
• food + music festival
• AUGUST 11 & 12, 2018
• Cedarline Showgrounds at Harwick Meadow Park
• 50+ Local Restaurants & Food Trucks • Live Music
• Classic Car Show • Craft Beer & Cocktails
• Kids Activities & More!
• (small) Produced by (Brindle Oak Publishing Logo)
• Design style: Think, modern, hip, fun, local
Nice to have
• small area for sponsor logos
Should not have
• Design style: NOT county fair

```html
<!DOCTYPE html>
<html lang="en">
<head>
<meta charset="utf-8">
<title>SAVOR Food + Music Festival Poster</title>
<link rel="stylesheet" href="https://fonts.googleapis.com/css2?family=Dosis:wght@500;600;700;800&display=swap">
<style>
  :root {
    --pink: #e6357f;
    --magenta: #d8348f;
    --orange: #f3923f;
    --purple: #8a5cc0;
    --teal: #5fc6bd;
    --mint: #86d2bf;
    --white: #ffffff;
    --red: #e8232b;
    --ink: #1c1c1c;
    --frame: #ffffff;
  }
  * { margin: 0; padding: 0; box-sizing: border-box; }
  html, body { width: 776px; height: 1200px; overflow: hidden; }
  body { font-family: "Dosis", sans-serif; }

  .poster {
    position: relative;
    width: 776px;
    height: 1200px;
    overflow: hidden;
    background:
      radial-gradient(ellipse 420px 380px at 40px 420px, rgba(245,150,60,.85), rgba(245,150,60,0) 70%),
      radial-gradient(ellipse 380px 420px at 790px 360px, rgba(135,90,200,.85), rgba(135,90,200,0) 70%),
      linear-gradient(180deg, var(--magenta) 0%, var(--pink) 22%, #e87a8a 45%, #b9a7b8 62%, var(--mint) 80%, var(--teal) 100%);
  }

  /* Brand */
  .brand { position: absolute; top: 24px; left: 0; width: 100%; text-align: center; color: var(--white); }
  .brand-mark {
    display: block; width: 132px; height: 132px; margin: 0 auto;
    border: 11px solid var(--white); border-radius: 50%;
  }
  .brand-name { display: block; margin-top: 8px; font-size: 42px; font-weight: 600; letter-spacing: 5px; line-height: 1; }
  .festival-title { margin-top: 16px; font-weight: 600; line-height: .9; }
  .festival-title .line1 { display: block; font-size: 66px; letter-spacing: -1px; }
  .festival-title .line2 { display: block; font-size: 70px; letter-spacing: 2px; margin-top: 2px; }

  /* Producer */
  .producer { position: absolute; top: 30px; left: 640px; width: 118px; text-align: center; }
  .producer-label { font-size: 12px; font-weight: 800; color: var(--ink); letter-spacing: .5px; }
  .producer-badge {
    width: 110px; height: 110px; margin: 4px auto 0; border-radius: 50%;
    background: var(--ink); display: flex; align-items: center; justify-content: center;
    color: var(--white); font-size: 14px; font-weight: 800; line-height: 1.15; padding: 12px;
  }

  /* Photo collage */
  .photo {
    position: absolute; border: 6px solid var(--frame);
    box-shadow: 0 2px 6px rgba(0,0,0,.25);
  }
  .photo-grill { left: 26px; top: 522px; width: 204px; height: 226px; transform: rotate(-2deg);
    background: linear-gradient(160deg, #2a2622, #6b4a36 55%, #d9cfc0); }
  .photo-eater { left: 114px; top: 382px; width: 306px; height: 232px; transform: rotate(-1deg);
    background: linear-gradient(180deg, #9cc0e0 0%, #7e9a6c 45%, #7a6a62 100%); }
  .photo-drink { left: 406px; top: 372px; width: 312px; height: 220px; transform: rotate(-2deg);
    background: linear-gradient(120deg, #c9d6e0, #86a2bf 50%, #3c6fa8); }
  .photo-hoop { left: 462px; top: 548px; width: 296px; height: 212px; transform: rotate(-1deg);
    background: linear-gradient(180deg, #b8c8d4 0%, #7f9a6a 35%, #5e8c3e 100%); }
  .photo-sandwich { left: 222px; top: 612px; width: 246px; height: 162px; transform: rotate(1deg);
    background: linear-gradient(135deg, #e0c79a, #b8844c 50%, #8a9a4a); }

  /* Event details */
  .event-info { position: absolute; top: 796px; left: 0; width: 100%; text-align: center; color: var(--red); font-weight: 800; line-height: 1; }
  .event-date { font-size: 50px; letter-spacing: .5px; }
  .event-venue { margin-top: 8px; font-size: 33px; letter-spacing: .5px; }
  .event-park { margin-top: 6px; font-size: 33px; letter-spacing: .5px; }

  .sponsor-area {
    position: absolute; left: 26px; top: 938px; width: 724px; height: 130px;
    border: 2px solid #2b3a3a; display: flex; align-items: center; justify-content: center;
    font-size: 23px; font-weight: 800; color: var(--ink); letter-spacing: .3px;
  }

  .highlights { position: absolute; top: 1076px; font-size: 22px; font-weight: 800; color: var(--ink); text-align: center; line-height: 1.25; }
  .highlights-left { left: 24px; width: 320px; }
  .highlights-right { left: 454px; width: 320px; }
  .highlights-bottom { position: absolute; top: 1148px; left: 0; width: 100%; text-align: center; font-size: 22px; font-weight: 800; color: var(--ink); }
</style>
</head>
<body>
<main class="poster">
  <header class="brand">
    <span class="brand-mark" aria-hidden="true"></span>
    <span class="brand-name">SAVOR</span>
    <h1 class="festival-title">
      <span class="line1">FOOD+MUSIC</span>
      <span class="line2">FESTIVAL</span>
    </h1>
  </header>

  <aside class="producer">
    <div class="producer-label">PRODUCED BY</div>
    <div class="producer-badge">Brindle Oak Publishing</div>
  </aside>

  <section class="collage">
    <div class="photo photo-grill" role="img" aria-label="Bacon and cheese topped burgers cooking on a grill"></div>
    <div class="photo photo-eater" role="img" aria-label="Festival-goer in sunglasses taking a bite of a sandwich outdoors"></div>
    <div class="photo photo-drink" role="img" aria-label="Hand holding up a can of craft beer at the festival"></div>
    <div class="photo photo-hoop" role="img" aria-label="Woman spinning a hula hoop on the festival lawn"></div>
    <div class="photo photo-sandwich" role="img" aria-label="Close-up of stacked sub sandwiches on a plate"></div>
  </section>

  <section class="event-info">
    <p class="event-date">AUGUST 11-12, 2018</p>
    <p class="event-venue">CEDARLINE SHOWGROUNDS</p>
    <p class="event-park">@HARWICK MEADOW PARK</p>
  </section>

  <div class="sponsor-area">YOUR SPONSOR LOGO HERE</div>

  <p class="highlights highlights-left">50+ LOCAL RESTAURANTS<br>&amp; FOOD TRUCKS • LIVE MUSIC</p>
  <p class="highlights highlights-right">CLASSIC CAR SHOW<br>• CRAFT BEER &amp; COCKTAILS</p>
  <p class="highlights-bottom">KIDS ACTIVITIES &amp; MORE!</p>
</main>
</body>
</html>
```